Packaging Design Project

I need a box for a hair oil called NEL. 3 color, Simple design .. We are open to new ideas, the over all theme.. Pure and Simple , Natural, Color protect, good for the hair. We started with a basic design and this is the existing website http://nelhaircare.com/

Industry/Entity Type

Hair

```html
<!DOCTYPE html>
<html lang="en">
<head>
<meta charset="utf-8">
<title>NEL Protective Hair Oil – Box Panel</title>
<link rel="stylesheet" href="https://fonts.googleapis.com/css2?family=Cinzel:wght@600;700&family=Tinos:wght@400&display=swap">
<style>
  :root {
    --cream: #f4ead8;
    --wine: #a31a2c;
    --wine-deep: #8e1424;
    --band: #a6202f;
    --band-text: #f7eee0;
    --ink: #1e1a18;
    --frame: #3a3330;
  }
  html, body {
    margin: 0;
    padding: 0;
    width: 1200px;
    height: 3016px;
    overflow: hidden;
    background: var(--cream);
  }
  .panel {
    position: relative;
    width: 1200px;
    height: 3016px;
    box-sizing: border-box;
    border: 5px solid var(--frame);
    background: var(--cream);
    overflow: hidden;
  }
  .brand-name {
    position: absolute;
    top: 470px;
    left: 0;
    width: 100%;
    text-align: center;
    margin: 0;
    font-family: "Cinzel", serif;
    font-weight: 700;
    font-size: 290px;
    line-height: 1;
    color: var(--wine);
    letter-spacing: 6px;
  }
  .rule {
    position: absolute;
    left: 110px;
    width: 980px;
    height: 6px;
    background: var(--wine);
  }
  .rule--top { top: 1400px; }
  .rule--bottom { top: 2288px; }
  .product-title {
    position: absolute;
    top: 1440px;
    left: 0;
    width: 100%;
    margin: 0;
    text-align: center;
    font-family: "Cinzel", serif;
    font-weight: 700;
    color: var(--wine);
    text-shadow: 3px 4px 5px rgba(60, 10, 15, 0.45);
    line-height: 1;
  }
  .product-title span { display: block; }
  .title-protective { font-size: 112px; margin-bottom: 40px; }
  .title-hair-oil  { font-size: 158px; margin-bottom: 30px; }
  .title-treatment { font-size: 106px; margin-bottom: 42px; }
  .title-and       { font-size: 58px;  margin-bottom: 40px; }
  .title-styling   { font-size: 118px; }
  .net-volume {
    position: absolute;
    top: 2700px;
    left: 0;
    width: 100%;
    text-align: center;
    font-family: "Tinos", serif;
    font-size: 54px;
    color: var(--ink);
  }
  .benefit-band {
    position: absolute;
    left: 0;
    bottom: 0;
    width: 100%;
    height: 240px;
    background: var(--band);
    display: flex;
    flex-direction: column;
    justify-content: center;
    align-items: center;
    font-family: "Tinos", serif;
    font-size: 74px;
    line-height: 1.3;
    color: var(--band-text);
  }
</style>
</head>
<body>
  <main class="panel">
    <h1 class="brand-name">NEL</h1>

    <div class="rule rule--top"></div>
    <h2 class="product-title">
      <span class="title-protective">PROTECTIVE</span>
      <span class="title-hair-oil">HAIR OIL</span>
      <span class="title-treatment">TREATMENT</span>
      <span class="title-and">AND</span>
      <span class="title-styling">STYLING AID</span>
    </h2>
    <div class="rule rule--bottom"></div>

    <p class="net-volume">100 ml / 3.4 oz</p>

    <footer class="benefit-band">
      <span>style, smooth</span>
      <span>shine &amp; condition</span>
    </footer>
  </main>
</body>
</html>
```